Eneginering consultancy brochure style web design project

Looking for a new brochure style web page for our small engineering consultancy. The prupose of the website is to provide some basic information with about the company, including exampels of our work, and present a way to initiate contact. There there will only be a few pages (up to 5) and limited content.A main focus of the project is to develop the visual design/identity for the webpage, and to provide the template for us to add content, rearrange layout and modify pages with relative ease.A mixture of text and images will be used. The use of an image slider would be desirable.We have recently had a new company logo developed (uploaded), which defines the colour scheme for the page.A professional. clean look is desired, that is not cluttered and easy to navigate.Template to add a photo slider is desirable.The use of swirl patterns (suach as those used here: https://www.brightvortex.co.uk/) and/or contoured mesh pattern (example attached) within the page is likely to be attractive, as this is in harmony with our activities.

Target Market(s)

Engineering; manufacturing

Industry/Entity Type

Engineering Consultant

Coding

Coded - Design and coding required

Number of Pages Required

3 page

Font styles to use
Other font styles liked:
• Helvetica

Colors
00a990
33b8a4
86cfc6
606060
3176b5
0255a3
85acd3
474747
7f7f7f

Requirements
Must have
• 1) Landing page for information about the company. Mostly text, with image slider.
• 2) One page for example projects. Images with accompanying texts.
• 3) Enquiry/'get in touch' page.
• Simple, uncluttered look and feel.

```html
<!DOCTYPE html>
<html lang="en">
<head>
<meta charset="utf-8">
<title>Kelvar Thermal Systems</title>
<link href="https://fonts.googleapis.com/css2?family=Montserrat:wght@700;800;900&family=Arimo:wght@400;700&display=swap" rel="stylesheet">
<style>
:root{
  --teal:#00a990;--teal2:#33b8a4;--teal3:#86cfc6;
  --blue:#0255a3;--blue2:#3176b5;--blue3:#85acd3;
  --grey:#606060;--dark:#474747;--mid:#7f7f7f;--white:#fff;
  --head:'Montserrat',sans-serif;--body:'Arimo',Helvetica,Arial,sans-serif;
}
*{margin:0;padding:0;box-sizing:border-box}
html,body{width:1200px;height:3838px;overflow:hidden;background:#fff}
.page{position:relative;width:1200px;height:3838px;overflow:hidden;font-family:var(--body);color:var(--grey)}
.abs{position:absolute}
.hero{left:0;top:0;width:1200px;height:800px;background:linear-gradient(120deg,#1a6fb8 0%,#0a5aa6 45%,#0e6a9c 75%,#1f8aa0 100%)}
.hero-wave{left:0;top:520px}
.brand{left:113px;top:0;width:195px;height:125px;background:#fff;display:flex;align-items:center;justify-content:center;gap:8px;font-family:var(--head);font-weight:800;font-size:17px;color:var(--blue);text-align:center;line-height:1.2}
.brand i{width:14px;height:14px;border-radius:50%;background:var(--teal);display:block;flex:none}
.nav{left:595px;top:48px;display:flex;gap:36px;font-size:19px;color:#fff}
.hero-title{right:112px;top:258px;text-align:right;font-family:var(--head);font-weight:800;font-size:33px;line-height:55px;letter-spacing:2px;color:#fff}
.btn{display:flex;align-items:center;justify-content:center;gap:6px;border-radius:30px;font-family:var(--body);font-weight:700}
.btn b{width:15px;height:15px;border-radius:50%;display:inline-flex;align-items:center;justify-content:center;font-size:10px}
.get{left:850px;top:463px;width:238px;height:62px;background:#fff;color:var(--blue);font-size:21px}
.get b{background:var(--blue);color:#fff}
.play{left:113px;top:652px;width:100px;height:100px;border-radius:50%;background:#fff;border:6px solid #dde3ea;box-shadow:0 2px 8px rgba(0,0,0,.15)}
.play svg{position:absolute;left:22px;top:22px}
.watch{left:218px;top:688px;font-family:var(--head);font-weight:800;font-size:18px;letter-spacing:1px;color:var(--teal);text-decoration:underline}
.about-img{left:113px;top:863px;width:439px;height:405px;background:linear-gradient(135deg,#4a6a86,#233849 55%,#7d8d99)}
.about-dot{left:418px;top:863px;width:134px;height:120px;background:var(--teal);border-radius:0 0 0 120px}
h2{font-family:var(--head);font-weight:900;color:#111;font-size:40px;letter-spacing:2px}
.about-title{left:625px;top:855px}
.about-text{left:625px;top:930px;width:463px;font-size:13.5px;line-height:24px;text-align:justify;color:var(--mid)}
.about-text p{margin-bottom:12px}
.read{left:625px;top:1228px;width:167px;height:46px;background:var(--teal);color:#fff;font-size:15px}
.read b{background:#fff;color:var(--teal)}
.serv-bg{left:520px;top:1350px}
.serv-title{left:113px;top:1455px}
.serv-text{left:113px;top:1540px;width:390px;font-size:14px;line-height:25px;text-align:justify;color:var(--mid)}
.link{font-weight:700;font-size:15px;color:var(--teal);text-decoration:underline}
.serv-link{left:113px;top:1678px}
.arrow{width:40px;height:40px;border-radius:50%;background:#fff;box-shadow:0 1px 6px rgba(0,0,0,.3);display:flex;align-items:center;justify-content:center;font-size:20px;color:#222}
.service{width:200px;text-align:center;font-size:21px;color:#222}
.service .ic{width:86px;height:86px;margin:0 auto 14px;border-radius:50%;background:radial-gradient(circle at 40% 35%,var(--teal2),#0a7a8c 70%,var(--blue));display:flex;align-items:center;justify-content:center}
.soft{left:0;top:1800px}
.soft-title{left:0;width:1200px;top:2018px;text-align:center;font-family:var(--head);font-weight:800;font-size:38px;letter-spacing:2px;color:#fff}
.soft-text{left:0;width:1200px;top:2088px;text-align:center;font-size:19px;line-height:30px;color:#fff}
.enq{left:510px;top:2168px;width:182px;height:45px;background:#fff;color:var(--blue);font-size:16px}
.enq b{background:var(--blue);color:#fff}
.partner{top:2358px;width:210px;height:92px;border:1px solid #ccd;display:flex;align-items:center;justify-content:center;gap:10px;font-size:22px;font-weight:700;color:#222}
.partner i{width:26px;height:26px;background:var(--blue);display:block}
.rule{left:113px;width:975px;height:1px;background:#d6dbe0}
.works-title{left:0;width:1200px;top:2648px;text-align:center}
.work{top:2738px;width:232px;height:192px}
.dots{left:525px;top:2980px;display:flex;gap:8px}
.dots span{width:32px;height:4px;background:#9aa;border-radius:2px}
.dots span.on{background:var(--teal)}
.foot{left:0;top:3040px}
.nl-title{left:113px;top:3183px;font-weight:700;font-size:18px;color:#fff;letter-spacing:.5px}
.nl-text{left:113px;top:3232px;width:360px;font-size:13.5px;line-height:25px;color:#fff}
.nl-form{left:113px;top:3303px;width:362px;height:44px;border:1px solid #fff;border-radius:24px;color:#fff;font-size:12px;padding-left:26px;display:flex;align-items:center}
.nl-btn{left:358px;top:3305px;width:116px;height:40px;background:#fff;color:var(--blue);font-size:13px}
.rule2{left:113px;top:3420px;width:975px;height:1px;background:rgba(255,255,255,.25)}
.col-h{top:3497px;font-weight:700;font-size:15.5px;color:#fff;letter-spacing:.5px}
.col{top:3540px;font-size:13.5px;line-height:24px;color:#fff;list-style:none}
.col li::before{content:"»";margin-right:18px}
.contact{left:113px;top:3540px;font-size:13.5px;line-height:24px;color:#fff}
.contact div{display:flex;gap:18px;margin-bottom:14px}
.contact svg{flex:none;margin-top:5px}
.social{left:922px;top:3537px;display:flex;gap:11px}
.social span{width:33px;height:33px;border:2px solid #fff;border-radius:50%}
.copy{left:0;width:1200px;top:3762px;text-align:center;font-size:15px;color:#fff}
</style>
</head>
<body>
<div class="page">
  <div class="abs hero" role="img" aria-label="Engineer operating industrial machinery in a workshop, tinted blue"></div>
  <svg class="abs hero-wave" width="1200" height="300" viewBox="0 0 1200 300">
    <path d="M0 20 C200 170 420 60 640 150 C850 240 1000 260 1200 80 L1200 300 L0 300Z" fill="#2dae9e" opacity=".85"/>
    <path d="M0 40 C200 190 420 80 640 170 C850 255 1020 270 1200 110 L1200 300 L0 300Z" fill="#fff"/>
  </svg>
  <div class="abs brand"><i></i>KTS<br>Kelvar Thermal</div>
  <nav class="abs nav"><span>HOME</span><span>ABOUT US</span><span>SERVICES</span><span>CONTACT US</span></nav>
  <h1 class="abs hero-title">THERMAL DESIGN,<br>SIMULATIONS &amp; ANALYSIS OF<br>ELECTRICAL MACHINES</h1>
  <div class="abs btn get">GET IN TOUCH <b>➜</b></div>

  <div class="abs play"><svg width="44" height="44" viewBox="0 0 44 44"><circle cx="22" cy="22" r="22" fill="#00a990"/><path d="M16 12 L33 22 L16 32Z" fill="#fff"/></svg></div>
  <div class="abs watch">WATCH VIDEO</div>

  <div class="abs about-img" role="img" aria-label="Engineer in hard hat with laptop beside a milling machine"></div>
  <div class="abs about-dot"></div>
  <h2 class="abs about-title">ABOUT US</h2>
  <div class="abs about-text">
    <p>KTS is a thermal engineering consultancy, specialising in the thermal design, simulation and analysis of electrical machines.</p>
    <p>Our experience spans across traditional and novel machine arrangements, with extensive experience with Permanent Magnet, Induction, Synchronous, Switched Reluctance and Synchronous Reluctance machines.</p>
    <p>Machines have been designed to operate in a range of applications and environments including automotive, aerospace, marine, energy generation and energy recovery.</p>
  </div>
  <div class="abs btn read">READ MORE <b>➜</b></div>

  <svg class="abs serv-bg" width="680" height="420" viewBox="0 0 680 420">
    <defs><linearGradient id="sg" x1="0" x2="1"><stop offset="0" stop-color="#e8f3f2"/><stop offset="1" stop-color="#d3ebe8"/></linearGradient></defs>
    <path d="M0 200 C200 40 450 60 680 0 L680 260 C450 300 200 380 0 330Z" fill="url(#sg)"/>
  </svg>
  <h2 class="abs serv-title">SERVICES</h2>
  <p class="abs serv-text">KTS offers thermal analysis and design for electrical machine design projects. We use a range of both commercial and in-house software for the design and optimisation of electrical machines using a multi-physics approach.</p>
  <a class="abs link serv-link">READ MORE ➜</a>
  <div class="abs arrow" style="left:1080px;top:1473px">‹</div>
  <div class="abs arrow" style="left:1133px;top:1473px">›</div>
  <div class="abs service" style="left:616px;top:1547px"><div class="ic"><svg width="40" height="34"><rect x="2" y="2" width="36" height="24" rx="2" fill="none" stroke="#fff" stroke-width="3"/><path d="M12 32h16" stroke="#fff" stroke-width="3"/></svg></div>Software Design</div>
  <div class="abs service" style="left:817px;top:1547px"><div class="ic"><svg width="40" height="40"><circle cx="20" cy="20" r="9" fill="none" stroke="#fff" stroke-width="3"/><path d="M20 3v8M20 29v8M3 20h8M29 20h8" stroke="#fff" stroke-width="3"/></svg></div>Machine Design</div>
  <div class="abs service" style="left:1010px;top:1547px"><div class="ic"><svg width="40" height="40"><rect x="6" y="4" width="28" height="32" rx="3" fill="none" stroke="#fff" stroke-width="3"/><path d="M12 14h16M12 21h16M12 28h10" stroke="#fff" stroke-width="3"/></svg></div>Software Project</div>

  <svg class="abs soft" width="1200" height="490" viewBox="0 0 1200 490">
    <defs><linearGradient id="bg" x1="0" x2="1" y1="0" y2="1"><stop offset="0" stop-color="#1a66b0"/><stop offset=".6" stop-color="#1d7fb0"/><stop offset="1" stop-color="#19ad98"/></linearGradient></defs>
    <path d="M0 20 C250 -20 450 80 650 150 C850 40 1050 0 1200 60 L1200 490 L0 490Z" fill="url(#bg)"/>
    <path d="M650 150 C850 40 1050 0 1200 60 L1200 120 C1030 80 850 110 650 150Z" fill="#33b8a4" opacity=".7"/>
  </svg>
  <div class="abs soft-title">SOFTWARE</div>
  <p class="abs soft-text">We are experienced with many different software packages, enabling us to select<br>the most appropriate tools for each project.</p>
  <div class="abs btn enq">ENQUIRY NOW <b>➜</b></div>

  <div class="abs partner" style="left:145px">Fluxa Solver</div>
  <div class="abs partner" style="left:378px">Matrica</div>
  <div class="abs partner" style="left:612px">OpenFlowCFD</div>
  <div class="abs partner" style="left:846px"><i style="border-radius:50%"></i></div>

  <div class="abs rule" style="top:2553px"></div>
  <h2 class="abs works-title">OUR WORKS</h2>
  <div class="abs work" style="left:113px;background:linear-gradient(135deg,#3b4856,#8a96a2)" role="img" aria-label="Machined metal components on a workbench"></div>
  <div class="abs work" style="left:361px;background:linear-gradient(135deg,#2b3a4a,#c07a45)" role="img" aria-label="Welding work with sparks"></div>
  <div class="abs work" style="left:608px;background:linear-gradient(135deg,#5a4a3a,#2f5e96)" role="img" aria-label="Technicians assembling machinery"></div>
  <div class="abs work" style="left:856px;background:linear-gradient(135deg,#2a2f36,#9aa1a8)" role="img" aria-label="Gloved hands testing electrical equipment"></div>
  <div class="abs dots"><span></span><span></span><span class="on"></span><span></span></div>

  <svg class="abs foot" width="1200" height="798" viewBox="0 0 1200 798">
    <defs><linearGradient id="fg" x1="0" x2="1"><stop offset="0" stop-color="#0e5fad"/><stop offset="1" stop-color="#1667b3"/></linearGradient></defs>
    <path d="M0 120 C250 -10 500 40 700 190 C880 300 1060 220 1200 120 L1200 798 L0 798Z" fill="#1fa897"/>
    <path d="M0 140 C250 10 500 60 700 210 C880 315 1060 240 1200 140 L1200 798 L0 798Z" fill="url(#fg)"/>
  </svg>
  <div class="abs nl-title">NEWSLETTER SUBSCRIPTION</div>
  <p class="abs nl-text">Register your Email Address to get More Information About Our Company &amp; Offers.</p>
  <div class="abs nl-form">Email Address</div>
  <div class="abs btn nl-btn">SUBSCRIBE</div>
  <div class="abs rule2"></div>

  <div class="abs col-h" style="left:113px">CONTACT US</div>
  <div class="abs contact">
    <div><svg width="12" height="16" viewBox="0 0 12 16"><path d="M6 0a6 6 0 0 1 6 6c0 4-6 10-6 10S0 10 0 6a6 6 0 0 1 6-6z" fill="#fff"/><circle cx="6" cy="6" r="2" fill="#0e5fad"/></svg><span>Riverside Science Park<br>Mill Road, Derford, DF4 2TU.</span></div>
    <div><svg width="14" height="14" viewBox="0 0 14 14"><path d="M3 0l3 3-2 2c1 2 3 4 5 5l2-2 3 3-2 3C6 14 0 8 0 3z" fill="#fff"/></svg><span>+44 (0)7700 900 412</span></div>
    <div><svg width="14" height="11" viewBox="0 0 14 11"><rect width="14" height="11" fill="#fff"/><path d="M0 0l7 6 7-6" fill="none" stroke="#0e5fad"/></svg><span>enquiries@kelvarthermal.com</span></div>
  </div>
  <div class="abs col-h" style="left:508px">CUSTOMER CARE</div>
  <ul class="abs col" style="left:508px"><li>Home</li><li>About Us</li><li>Services</li><li>FAQs</li><li>Help</li><li>Contact Us</li></ul>
  <div class="abs col-h" style="left:725px">OTHER LINKS</div>
  <ul class="abs col" style="left:725px"><li>Blog Post</li><li>Careers</li><li>Software</li><li>Privacy Policy</li></ul>
  <div class="abs col-h" style="left:922px">SOCIAL MEDIA</div>
  <div class="abs social"><span></span><span></span><span></span><span></span></div>
  <div class="abs copy">© CopyRight 2019 Kelvar Thermal Systems. All Rights Reserved.</div>
</div>
</body>
</html>
```